Business Card design for a skin clinic

i would like a business card design for our skin clinic.
our logo colors are Blue and Grey and Bule /white.
we are searching for a minimalistic design yet very elegant,dynamic and professional which can reflect a professional medical skin care clinic( not a beauty salon).
THE DESGIN IS NOT FOR A PERSON IT WILL BE USED IN THE CLINIC FOR CLIENTS SO THERE SHOULD BE NO NAME OF A PERSON ONLY THE CLINIC NAME AND THE CONTACT INFO

Target Market(s)
young and old womens
Industry/Entity Type
Business
Contact Information for Business Card
we have 2 address and both should be on the card.
address A: Lindenhofkade 42B, 3017KP Rotterdam, Tel 010 438 21 95
address B: Zonnewijzerstraat 73, 1062HT Amsterdam Tel 020 519 8372
website www.velorahuid.nu, email info@velorahuid.nu
Look and feel

```html
<!DOCTYPE html>
<html lang="nl">
<head>
<meta charset="utf-8">
<title>Velora Huid – Business Card</title>
<link rel="stylesheet" href="https://fonts.googleapis.com/css2?family=Jost:wght@400;500&family=PT+Serif&display=swap">
<style>
  :root {
    --backdrop: #e4e4e6;
    --ink: #1f1f21;
    --panel-dark: #262628;
    --brand-blue: #2a86c8;
    --brand-blue-deep: #1f6fae;
    --brand-grey: #5c5e62;
    --paper: #ffffff;
    --faint: #d3d4d6;
    --contact-text: #e9eaec;
  }
  * { margin: 0; padding: 0; box-sizing: border-box; }
  html, body { width: 1200px; height: 675px; overflow: hidden; }
  body {
    background: var(--backdrop);
    font-family: "Jost", "Helvetica Neue", Arial, sans-serif;
    position: relative;
  }
  .card {
    position: absolute;
    top: 189px;
    width: 520px;
    height: 297px;
    overflow: hidden;
    box-shadow: 0 6px 18px rgba(0,0,0,0.12);
  }
  .card--front { left: 60px; background: var(--ink); }
  .card--back { left: 620px; background: var(--paper); }

  .wordmark {
    position: absolute;
    text-align: center;
    line-height: 1;
  }
  .wordmark__name {
    font-family: "Jost", "Helvetica Neue", Arial, sans-serif;
    font-weight: 500;
    letter-spacing: 0.04em;
    display: flex;
    align-items: center;
    justify-content: center;
    gap: 0.4em;
  }
  .wordmark__dot {
    display: inline-block;
    width: 0.42em;
    height: 0.42em;
    border-radius: 50%;
    background: currentColor;
  }
  .wordmark__tagline {
    font-family: "PT Serif", Georgia, serif;
    margin-top: 0.4em;
  }

  .card--front .wordmark { left: 0; right: 0; top: 116px; }
  .card--front .wordmark__name { font-size: 38px; color: var(--brand-blue); }
  .card--front .wordmark__tagline { font-size: 19px; color: #f2f2f2; }

  .card--back .wordmark--top { left: 30px; width: 230px; top: 48px; }
  .card--back .wordmark--top .wordmark__name { font-size: 22px; color: var(--brand-blue); }
  .card--back .wordmark--top .wordmark__tagline { font-size: 11px; color: var(--brand-grey); }

  .band-blue {
    position: absolute;
    left: 0; top: 150px;
    width: 262px; height: 112px;
    background: linear-gradient(90deg, var(--brand-blue) 0%, var(--brand-blue-deep) 100%);
  }
  .band-blue__notch {
    position: absolute;
    left: 136px; top: 150px;
    width: 0; height: 0;
    border-left: 9px solid transparent;
    border-right: 9px solid transparent;
    border-top: 9px solid var(--paper);
  }
  .card--back .wordmark--band { left: 10px; width: 230px; top: 188px; }
  .card--back .wordmark--band .wordmark__name { font-size: 22px; color: var(--paper); }
  .card--back .wordmark--band .wordmark__tagline { font-size: 11px; color: var(--paper); }

  .panel-dark {
    position: absolute;
    left: 250px; top: 92px;
    width: 270px; height: 110px;
    background: var(--panel-dark);
    z-index: 1;
  }
  .panel-dark__pointer {
    position: absolute;
    left: 242px; top: 176px;
    width: 0; height: 0;
    border-top: 8px solid transparent;
    border-bottom: 8px solid transparent;
    border-right: 8px solid var(--panel-dark);
    z-index: 1;
  }
  .contact-list {
    position: absolute;
    left: 268px; top: 102px;
    list-style: none;
    font-family: "PT Serif", Georgia, serif;
    font-size: 9.5px;
    color: var(--contact-text);
    z-index: 2;
  }
  .contact-list li {
    display: flex;
    align-items: center;
    gap: 7px;
    height: 15px;
    white-space: nowrap;
  }
  .contact-icon { width: 9px; height: 9px; flex: none; }

  .faint-name {
    position: absolute;
    left: 290px; top: 224px;
    font-size: 15px;
    font-weight: 400;
    letter-spacing: 0.05em;
    color: var(--faint);
  }
</style>
</head>
<body>
  <section class="card card--front" aria-label="Card front">
    <div class="wordmark">
      <div class="wordmark__name"><span class="wordmark__dot"></span>VELORA HUID</div>
      <div class="wordmark__tagline">medical dermatology clinic</div>
    </div>
  </section>

  <section class="card card--back" aria-label="Card back">
    <div class="wordmark wordmark--top">
      <div class="wordmark__name">VELORA HUID</div>
      <div class="wordmark__tagline">medical dermatology clinic</div>
    </div>

    <div class="band-blue"></div>
    <div class="band-blue__notch"></div>
    <div class="wordmark wordmark--band">
      <div class="wordmark__name">VELORA HUID</div>
      <div class="wordmark__tagline">medical dermatology clinic</div>
    </div>

    <div class="panel-dark"></div>
    <div class="panel-dark__pointer"></div>
    <ul class="contact-list">
      <li>
        <svg class="contact-icon" viewBox="0 0 10 10"><path d="M5 0.5a3.2 3.2 0 0 1 3.2 3.2C8.2 6 5 9.5 5 9.5S1.8 6 1.8 3.7A3.2 3.2 0 0 1 5 0.5z" fill="#cfd0d2"/><circle cx="5" cy="3.7" r="1.2" fill="#262628"/></svg>
        Lindenhofkade 42B, 3017KP Rotterdam
      </li>
      <li>
        <svg class="contact-icon" viewBox="0 0 10 10"><path d="M2 0.8l1.6 2.2-1 1c0.6 1.3 1.5 2.2 2.8 2.8l1-1 2.2 1.6-0.9 1.6C4.4 8.8 1.2 5.6 0.4 1.7z" fill="#cfd0d2"/></svg>
        010 438 21 95
      </li>
      <li>
        <svg class="contact-icon" viewBox="0 0 10 10"><path d="M5 0.5a3.2 3.2 0 0 1 3.2 3.2C8.2 6 5 9.5 5 9.5S1.8 6 1.8 3.7A3.2 3.2 0 0 1 5 0.5z" fill="#cfd0d2"/><circle cx="5" cy="3.7" r="1.2" fill="#262628"/></svg>
        Zonnewijzerstraat 73, 1062HT Amsterdam
      </li>
      <li>
        <svg class="contact-icon" viewBox="0 0 10 10"><path d="M2 0.8l1.6 2.2-1 1c0.6 1.3 1.5 2.2 2.8 2.8l1-1 2.2 1.6-0.9 1.6C4.4 8.8 1.2 5.6 0.4 1.7z" fill="#cfd0d2"/></svg>
        020 519 8372
      </li>
      <li>
        <svg class="contact-icon" viewBox="0 0 10 10"><rect x="0.5" y="2" width="9" height="6" fill="#cfd0d2"/><path d="M0.8 2.3L5 5.6 9.2 2.3" fill="none" stroke="#262628" stroke-width="0.9"/></svg>
        email info@velorahuid.nu
      </li>
      <li>
        <svg class="contact-icon" viewBox="0 0 10 10"><circle cx="5" cy="5" r="4.3" fill="none" stroke="#cfd0d2" stroke-width="0.9"/><ellipse cx="5" cy="5" rx="1.8" ry="4.3" fill="none" stroke="#cfd0d2" stroke-width="0.8"/><path d="M0.7 5h8.6" stroke="#cfd0d2" stroke-width="0.8"/></svg>
        www.velorahuid.nu
      </li>
    </ul>

    <div class="faint-name">VELORA HUID</div>
  </section>
</body>
</html>
```